Atelier Greta Voss Coming Soon

Launching a online mid century furniture business. I'm participating in an antiques fair prior to the website launch. I'd like a 1 page flyer that highlights a sampling of some iconic pieces and invites people to check out the website soon. If possible, I'd also like a Word template for a tear sheet (a one page doc that has the company logo and contact info, a picture of the item, a field for description and dimensions). The following is an example of a tear sheet...http://www.kbtcabinetworks.example/uploads/4/8/1/3/4813902/vesper_oak_low_side_chair.pdf. I'd prefer a smaller slot for the image (maybe one side of the page) and a much larger area for description and dimensions (as its vintage furniture I'll need to report on condition).

I've attached a few sample pieces of furniture, the company logo, contact information, and a room that included furniture from the business. The color palette for the business is orange, black, white and gray.

Target Market(s)

Potential Customers.....

Industry/Entity Type

Retail

Font styles to use
Other font styles liked:
• I think the fonts should be similar to the ones used in the logo and the business card (see attached)

Colors
f37122
1b1b1b
ebebeb

Requirements
Must have
• An elegant clean look and feel (although its a mid century furniture business I don't carry kitschy items...just really beautiful classic high-end pieces). It should highlight the beauty of the furniture and provide contact information.

```html
<!DOCTYPE html>
<html lang="en">
<head>
<meta charset="utf-8">
<title>Atelier Greta Voss — Tear Sheets</title>
<link rel="stylesheet" href="https://fonts.googleapis.com/css2?family=Arimo:wght@400;700&family=Antonio:wght@300&display=swap">
<style>
  :root {
    --orange: #d9773a;
    --ink: #1b1b1b;
    --band: #d9d9d9;
    --canvas: #f0f0f0;
    --shadow: #b3b3b3;
    --paper: #ffffff;
  }
  * { box-sizing: border-box; margin: 0; padding: 0; }
  html, body { width: 1200px; height: 849px; overflow: hidden; }
  body {
    background: var(--canvas);
    font-family: "Arimo", Arial, sans-serif;
    color: var(--ink);
    position: relative;
  }
  .sheet {
    position: absolute;
    top: 26px;
    width: 557px;
    height: 788px;
    background: var(--paper);
    box-shadow: 10px 10px 0 var(--shadow);
  }
  .sheet--left { left: 22px; }
  .sheet--right { left: 611px; }

  .sheet__header {
    position: absolute; top: 0; left: 0; right: 0;
    height: 68px;
    background: var(--band);
  }
  .sheet__title {
    position: absolute; right: 67px; top: 41px;
    font-size: 14px; font-weight: 700; line-height: 1;
  }
  .sheet__title::before {
    content: "||";
    color: var(--orange);
    font-weight: 400;
    margin-right: 9px;
  }
  .sheet__photo { position: absolute; }
  .sheet--left .sheet__photo { left: 69px; top: 112px; width: 422px; height: 276px;
    background: linear-gradient(180deg, #8a6a55 0%, #6b5548 22%, #2a1d18 45%, #241915 78%, #9c8672 100%); }
  .sheet--right .sheet__photo { left: 69px; top: 76px; width: 422px; height: 368px;
    background: linear-gradient(180deg, #6e4a44 0%, #5d4b48 20%, #b6a268 45%, #a8955e 70%, #8e8c86 100%); }

  .sheet__rule {
    position: absolute; left: 0; right: 0; top: 454px; height: 8px;
    border-top: 2.5px solid var(--orange);
    border-bottom: 2.5px solid var(--orange);
  }
  .sheet__dims {
    position: absolute; right: 67px; top: 473px;
    font-size: 12px;
  }
  .sheet__desc {
    position: absolute; left: 68px; width: 423px; top: 504px;
    font-size: 12px; line-height: 15.5px;
    text-align: justify;
  }
  .sheet__footer {
    position: absolute; left: 0; right: 0; bottom: 0;
    height: 149px;
    background: var(--band);
    text-align: center;
  }
  .brand {
    margin-top: 42px;
    font-family: "Antonio", "Oswald", sans-serif;
    font-weight: 300;
    font-size: 46px;
    line-height: 1;
    letter-spacing: 3px;
    color: var(--ink);
    text-transform: uppercase;
  }
  .contact {
    margin-top: 8px;
    font-size: 9.6px;
    white-space: nowrap;
  }
  .contact__web { color: var(--orange); font-weight: 700; }
  .contact__sep { color: var(--orange); margin: 0 3px; }
  .contact__phone { font-weight: 700; }
</style>
</head>
<body>

<article class="sheet sheet--left">
  <header class="sheet__header"><h1 class="sheet__title">Hallgren Buffet</h1></header>
  <div class="sheet__photo" role="img" aria-label="Photo of a dark-stained four-drawer, two-cabinet Asian style buffet with brass pulls against a brick wall"></div>
  <div class="sheet__rule"></div>
  <p class="sheet__dims">61"W × 21"D × 36.75"H</p>
  <p class="sheet__desc">Newly stained black, this four-drawer, two cabinet, Asian style buffet/sideboard was manufactured by Hallgren Furniture of Rockford, Illinois. Chinoiserie styling with aged copper and nickel drop Greek key pulls and trefoil escutcheons. Platform style four leg base.</p>
  <footer class="sheet__footer">
    <p class="brand">Atelier Greta Voss</p>
    <p class="contact"><span class="contact__web">www.ateliergretavoss.com</span><span class="contact__sep">||</span><span class="contact__phone">Office: +(312) 555 0147</span><span class="contact__sep">||</span>info@ateliergretavoss.com</p>
  </footer>
</article>

<article class="sheet sheet--right">
  <header class="sheet__header"><h1 class="sheet__title">Brightwork Chest</h1></header>
  <div class="sheet__photo" role="img" aria-label="Photo of a brass-clad chest of drawers with raised Asian characters as pulls against a brick wall"></div>
  <div class="sheet__rule"></div>
  <p class="sheet__dims">32"W × 29.5"D × 16"H</p>
  <p class="sheet__desc">1970s Vintage Brightwork chest of drawers with Asian characters as pull motif. Excellent. Compared to that other furniture-makers in historically minded Grand Rapids, Michigan, the work of Brightwork seems positively flamboyant.</p>
  <footer class="sheet__footer">
    <p class="brand">Atelier Greta Voss</p>
    <p class="contact"><span class="contact__web">www.ateliergretavoss.com</span><span class="contact__sep">||</span><span class="contact__phone">Office: +(312) 555 0147</span><span class="contact__sep">||</span>info@ateliergretavoss.com</p>
  </footer>
</article>

</body>
</html>
```